Unique business card design

We are looking for a design that reflects our unique social media and online marketing agency "Kestrel Media". We are a young agency with a focus on speakers, coaches and trainers. In other words, we support people who want to do good with their work and help other people live a happier, more successful and fulfilling life, reach as many people as possible with their work and thus have an influence. Our values are: sustainability, creating added value, individuality, proactivity. We want our clients to feel comfortable with us and that's why the relationship with them is very important to us. We want every customer to become a lifelong friend of the company. Most of our clients are premium coaches, meaning they are in the higher priced segment and expect seriousness, professionalism and quality. All of these things should reflect our business card as well. I look forward to feedback. Best regards, Tomas Wylander

```html
<!DOCTYPE html>
<html lang="en">
<head>
<meta charset="utf-8">
<title>Kestrel Media – Business Card</title>
<link rel="stylesheet" href="https://fonts.googleapis.com/css2?family=Lato:wght@400;700&family=Quicksand:wght@700&display=swap">
<style>
  :root {
    --backdrop: #9b9b9b;
    --card-white: #ffffff;
    --card-blue: #33349a;
    --navy: #0d0f6b;
    --azure: #1f6fc1;
    --ink: #2b2b2b;
    --rule: #b8b8b8;
    --white: #ffffff;
  }
  * { margin: 0; padding: 0; box-sizing: border-box; }
  html, body { width: 1200px; height: 900px; overflow: hidden; }
  body {
    position: relative;
    background: var(--backdrop);
    font-family: "Lato", Arial, sans-serif;
  }
  .card {
    position: absolute;
    top: 306px;
    height: 271px;
    box-shadow: 2px 3px 5px rgba(0, 0, 0, 0.45);
  }
  .card--front { left: 149px; width: 439px; background: var(--card-white); }
  .card--back  { left: 608px; width: 441px; background: var(--card-blue); }

  .brand {
    position: absolute;
    width: 190px;
    display: flex;
    flex-direction: column;
    gap: 9px;
  }
  .brand__row { display: flex; align-items: center; gap: 9px; }
  .brand__mark { width: 40px; height: 40px; background: var(--navy); flex: none; }
  .brand__name {
    font-family: "Lato", Arial, sans-serif;
    font-weight: 700;
    font-size: 22px;
    line-height: 26px;
    color: var(--navy);
    white-space: nowrap;
  }
  .brand__tagline {
    font-size: 12px;
    line-height: 15px;
    letter-spacing: 0.9px;
    color: var(--azure);
    white-space: nowrap;
  }
  .card--front .brand { left: 29px; top: 104px; }
  .card--back .brand { left: 122px; top: 104px; }
  .card--back .brand__mark { background: var(--white); }
  .card--back .brand__name,
  .card--back .brand__tagline { color: var(--white); }

  .divider {
    position: absolute;
    left: 238px;
    top: 64px;
    width: 1px;
    height: 142px;
    background: var(--rule);
  }
  .details { position: absolute; left: 259px; top: 59px; color: var(--ink); }
  .details__name {
    font-family: "Quicksand", Arial, sans-serif;
    font-weight: 700;
    font-size: 18px;
    color: var(--navy);
    line-height: 22px;
    white-space: nowrap;
  }
  .details__name span { color: var(--azure); }
  .details__role { font-size: 12px; line-height: 14px; margin-bottom: 10px; }
  .contact { list-style: none; font-size: 12.5px; line-height: 16.6px; }
  .contact li { display: flex; align-items: center; gap: 3px; white-space: nowrap; }
  .contact svg { width: 11px; height: 11px; flex: none; }
  .address { font-size: 12.5px; line-height: 16px; margin-top: 8px; white-space: nowrap; }
</style>
</head>
<body>
  <section class="card card--front">
    <div class="brand">
      <div class="brand__row">
        <div class="brand__mark"></div>
        <div class="brand__name">Kestrel Media</div>
      </div>
      <div class="brand__tagline">Online Marketing Services</div>
    </div>
    <div class="divider"></div>
    <div class="details">
      <div class="details__name">Tomas <span>Wylander</span></div>
      <div class="details__role">Managing Director</div>
      <ul class="contact">
        <li><svg viewBox="0 0 11 11"><rect width="11" height="11" fill="#0d0f6b"/><rect x="3.5" y="2" width="4" height="7" rx="0.6" fill="none" stroke="#fff" stroke-width="1"/></svg>044-123 456 789</li>
        <li><svg viewBox="0 0 11 11"><rect width="11" height="11" fill="#0d0f6b"/><path d="M2.5 4.5 Q5.5 2 8.5 4.5 L7.5 5.5 L6.5 4.7 L4.5 4.7 L3.5 5.5 Z M3.5 6 H7.5 V8.5 H3.5 Z" fill="#fff"/></svg>044-123 456 789</li>
        <li><svg viewBox="0 0 11 11"><rect width="11" height="11" fill="#0d0f6b"/><rect x="2.5" y="3.5" width="6" height="4.2" fill="none" stroke="#fff" stroke-width="0.9"/><path d="M2.5 3.5 L5.5 6 L8.5 3.5" fill="none" stroke="#fff" stroke-width="0.9"/></svg>hello@kestrelmedia.net</li>
        <li><svg viewBox="0 0 11 11"><rect width="11" height="11" fill="#0d0f6b"/><circle cx="5.5" cy="5.5" r="3" fill="none" stroke="#fff" stroke-width="0.9"/><path d="M2.5 5.5 H8.5 M5.5 2.5 V8.5" stroke="#fff" stroke-width="0.7"/></svg>www.kestrelmedia.net</li>
      </ul>
      <div class="address">12345, Address Goes Here<br>Country Name, 123456</div>
    </div>
  </section>

  <section class="card card--back">
    <div class="brand">
      <div class="brand__row">
        <div class="brand__mark"></div>
        <div class="brand__name">Kestrel Media</div>
      </div>
      <div class="brand__tagline">Online Marketing Services</div>
    </div>
  </section>
</body>
</html>
```